Electrical construction, completion and commissioning
Keystone Ridge Services
Use same font as used in my logo
not sure may try a few options
Professional
Callum Brody
Director
PO Box 7819 East Perth WA 6892
callum@keystoneridgeservices.com.au
keystoneridgeservices.com.au
EC 20735
ABN 48 271 502 936
Electrical Construction Engineering Completions Commissioning Management and Supervision

```html
<!DOCTYPE html>
<html lang="en">
<head>
<meta charset="utf-8">
<title>Keystone Ridge Services – Business Card</title>
<link rel="stylesheet" href="https://fonts.googleapis.com/css2?family=Michroma&family=Montserrat:wght@400;500&display=swap">
<style>
  :root {
    --bg: #d9dadb;
    --card-white: #ffffff;
    --brand-blue: #1f8fd6;
    --deep-blue: #0f6fc0;
    --light-blue: #3fb0ee;
    --brand-green: #7cc242;
    --ink: #4a4a4a;
    --ink-soft: #6b6b6b;
  }
  * { margin: 0; padding: 0; box-sizing: border-box; }
  html, body { width: 1200px; height: 895px; overflow: hidden; }
  body {
    background: var(--bg);
    font-family: "Montserrat", Arial, sans-serif;
    position: relative;
  }
  .card {
    position: absolute;
    width: 540px;
    height: 330px;
    border-radius: 4px;
    overflow: hidden;
    box-shadow: 0 10px 26px rgba(0,0,0,0.22);
  }
  .card--front { left: 45px; top: 300px; background: var(--card-white); }
  .card--back {
    left: 615px; top: 265px;
    background: radial-gradient(circle at 35% 25%, var(--light-blue) 0%, var(--brand-blue) 45%, var(--deep-blue) 100%);
  }

  /* Front */
  .brand {
    position: absolute; left: 40px; top: 46px;
    display: flex; align-items: center; gap: 14px;
  }
  .brand__dot {
    width: 52px; height: 52px; border-radius: 50%;
    background: var(--brand-green);
  }
  .brand__name {
    font-family: "Michroma", Arial, sans-serif;
    color: var(--brand-blue);
    font-size: 22px;
    line-height: 1.15;
    letter-spacing: 1px;
    text-transform: uppercase;
  }
  .person {
    position: absolute; left: 106px; top: 128px;
    font-variant: small-caps;
    letter-spacing: 1px;
  }
  .person__name { color: var(--brand-blue); font-size: 15px; font-weight: 500; }
  .person__role { color: var(--ink-soft); font-size: 12px; margin-top: 2px; }
  .address {
    position: absolute; left: 40px; top: 178px;
    font-size: 12px; line-height: 1.6; color: var(--ink);
    font-variant: small-caps; letter-spacing: 1px;
  }
  .contact {
    position: absolute; left: 228px; top: 170px;
    list-style: none;
    font-size: 11px; line-height: 1.9; color: var(--ink);
    font-variant: small-caps; letter-spacing: 0.6px;
  }
  .contact li { display: flex; align-items: center; gap: 7px; }
  .contact svg { width: 12px; height: 12px; flex: none; }
  .contact__phone { font-size: 13px; }
  .footer-band { position: absolute; left: 0; bottom: 0; width: 100%; height: 36px; }

  /* Back */
  .back__web {
    position: absolute; left: 0; right: 0; bottom: 56px;
    text-align: center;
    color: #ffffff;
    font-size: 15px;
    letter-spacing: 3px;
    font-variant: small-caps;
  }
</style>
</head>
<body>
  <section class="card card--front" aria-label="Business card front">
    <div class="brand">
      <span class="brand__dot"></span>
      <span class="brand__name">Keystone Ridge<br>Services</span>
    </div>

    <div class="person">
      <p class="person__name">Callum Brody</p>
      <p class="person__role">Director</p>
    </div>

    <p class="address">PO Box 7819<br>Westbrook WA 6915</p>

    <ul class="contact">
      <li class="contact__phone">
        <svg viewBox="0 0 12 12"><rect x="3" y="0.5" width="6" height="11" rx="1.2" fill="none" stroke="#1f8fd6" stroke-width="1.2"/><circle cx="6" cy="9.5" r="0.7" fill="#1f8fd6"/></svg>
        0412 736 905
      </li>
      <li>
        <svg viewBox="0 0 12 12"><rect x="0.6" y="2.5" width="10.8" height="7" fill="none" stroke="#1f8fd6" stroke-width="1.1"/><path d="M0.8 2.8 L6 6.8 L11.2 2.8" fill="none" stroke="#1f8fd6" stroke-width="1.1"/></svg>
        callum@keystoneridgeservices.com.au
      </li>
      <li>
        <svg viewBox="0 0 12 12"><circle cx="6" cy="6" r="5" fill="#1f8fd6"/></svg>
        callumbrody
      </li>
      <li>
        <svg viewBox="0 0 12 12"><circle cx="6" cy="6" r="5" fill="none" stroke="#1f8fd6" stroke-width="1.1"/><ellipse cx="6" cy="6" rx="2.2" ry="5" fill="none" stroke="#1f8fd6" stroke-width="1"/><path d="M1 6 H11" stroke="#1f8fd6" stroke-width="1"/></svg>
        www.keystoneridgeservices.com.au
      </li>
    </ul>

    <svg class="footer-band" viewBox="0 0 540 36" preserveAspectRatio="none" aria-hidden="true">
      <defs>
        <linearGradient id="bandBlue" x1="0" y1="0" x2="1" y2="0">
          <stop offset="0" stop-color="#0f6fc0"/>
          <stop offset="1" stop-color="#3fb0ee"/>
        </linearGradient>
        <linearGradient id="bandGreen" x1="0" y1="0" x2="1" y2="0">
          <stop offset="0" stop-color="#9ad158"/>
          <stop offset="1" stop-color="#5fae2e"/>
        </linearGradient>
      </defs>
      <polygon points="0,12 300,12 290,36 0,36" fill="url(#bandBlue)"/>
      <polygon points="306,0 540,0 540,36 290,36" fill="url(#bandGreen)"/>
      <polygon points="300,12 306,0 296,24" fill="#ffffff"/>
    </svg>
  </section>

  <section class="card card--back" aria-label="Business card back">
    <p class="back__web">www.keystoneridgeservices.com.au</p>
  </section>
</body>
</html>
```